依頼詳細
■商品の特徴
・使用する原材料は「小麦粉・塩・水」のみ。厳選した国産小麦粉をたっぷりの水で捏ね、みずみずしい透明感とツヤのある麺に仕上げました。
・麺の太さは、細すぎず、適度な噛みごたえ、食べ応えが楽しめます。
・油を使っていないシンプルな原材料で安心感も併せて訴求。

■デザインの方向性
・和紙(雲竜またはカルミナ)の風合いを生かす
・和モダン、シンプル、品がある、
・素朴で田舎っぽいがお洒落なイメージも想起させる。
・夏、涼しい、冷たい、水、流れ、波紋など、涼感を想起させるイメージ。
・商品名が筆文字の場合は、達筆すぎない、崩れすぎていない、読みやすいこと。

■留意点
・ジジ臭いのはNG(蕎麦やうどんは、とかくジジ臭くなりがちです)

■ 利用用途
・決定したデザインはそうめんの他、冷麦などシリーズ展開します。
記載項目
■パッケージ仕様
・商品名:青峰の細打ち冷や糸(仮名)
・フィルム寸法:W230×H275(オモテ面 W100×H275の範囲をデザイン)
・フィルム材質:レーヨン紙(雲竜またはカルミナ)
・色数:5色まで(シズルは無し)
希望イメージ
シンプル 複雑
単色 カラフル
暗い 明るい
日常 高級
遊び心 厳粛
未来的 伝統的
女性的 男性的
希望する色
青系、水色系、グレー系、紫系
納品ファイル
• 高解像度JPG (.jpg)
• イラストレーター形式 (.ai)
• フォトショップ形式 (.psd)
補足説明
合成用の画像を用意しましたので、可能であればこの画像に合成してご提案いただけますでしょか?よろしくお願い致します。
■ 選んだ理由

和風、モダンさのバランスが求めていたものに近い気がしました。売り場のイメージにもマッチしていると感じました。色を変えてのシリーズ展開もしやすそうでした。白を生かした涼感も感じました。

■ 提案者全員のお礼・コメント

この度は素敵なデザインのご提案ありがとうございます。こちらのデザインを元に修正もお願いするかと思います。その際はよろしくお願いいたします。
まずは、修正の方向性を私の方で探って見たいので、イラレのデータをいただけますでしょうか?よろしくお願いいたします。

```html
<!DOCTYPE html>
<html lang="ja">
<head>
<meta charset="UTF-8">
<title>青峰の細打ち冷や糸 パッケージ</title>
<link rel="stylesheet" href="https://fonts.googleapis.com/css2?family=Klee+One:wght@600&display=swap">
<style>
  :root {
    --paper: #f7fbfd;
    --stream-light: #e4f0f8;
    --stream-mid: #cfe3f1;
    --ink: #141414;
    --accent-blue: #6fa9d6;
    --badge: #ffffff;
  }
  html, body {
    margin: 0;
    padding: 0;
    width: 1200px;
    height: 2868px;
    overflow: hidden;
    background: var(--paper);
  }
  .package-front {
    position: relative;
    width: 1200px;
    height: 2868px;
    overflow: hidden;
    font-family: "Klee One", cursive;
  }
  .water-texture {
    position: absolute;
    inset: 0;
    background: linear-gradient(90deg,
      var(--stream-light) 0%,
      var(--paper) 18%,
      var(--stream-mid) 36%,
      var(--stream-light) 52%,
      var(--paper) 68%,
      var(--stream-mid) 84%,
      var(--stream-light) 100%);
  }
  .origin-badge {
    position: absolute;
    left: 780px;
    top: 160px;
    width: 380px;
    height: 380px;
    border-radius: 50%;
    background: var(--badge);
    display: flex;
    align-items: center;
    justify-content: center;
  }
  .origin-badge__text {
    writing-mode: vertical-rl;
    font-size: 92px;
    font-weight: 600;
    color: var(--accent-blue);
    letter-spacing: 4px;
    margin: 0;
  }
  .product-title {
    position: absolute;
    left: 480px;
    top: 500px;
    width: 240px;
    height: 2000px;
    margin: 0;
    writing-mode: vertical-rl;
    font-size: 220px;
    font-weight: 600;
    color: var(--ink);
    letter-spacing: 100px;
    line-height: 1;
    display: flex;
    align-items: center;
  }
</style>
</head>
<body>
  <main class="package-front">
    <div class="water-texture" role="img" aria-label="細い青の縦の流水線が全面に並ぶ涼しげな和紙風の背景模様"></div>
    <div class="origin-badge">
      <p class="origin-badge__text">青峰の</p>
    </div>
    <h1 class="product-title">細打ち冷や糸</h1>
  </main>
</body>
</html>
```